Sponsor at Title Insurance Industry Seminar for Continuing Ed - 250 Companies in Attendance

I offer escrow accounting services in the Title Insurance Industry. I've attached logo files and an example of my former company. I don't like the design and it's a little wordy but it provides detail of what I offer.

Below is a brief write-up...
For professionals in the title insurance industry, finding a reliable and cost-effective solution to escrow accounting needs can feel overwhelming. When choosing the right accounting partner, title companies and law firms need a group they can trust, and that’s where we come in. Brightfen Ledger Works is a team that understands the title industry and the importance of compliance, security and accuracy. Brightfen Ledger Works is the experienced, convenient and cost-effective choice for the accounting and certification needs of companies throughout the country.

```html
<!DOCTYPE html>
<html lang="en">
<head>
<meta charset="utf-8">
<title>Brightfen Ledger Works – Escrow Reconciliation Services</title>
<link rel="stylesheet" href="https://fonts.googleapis.com/css2?family=Poppins:wght@400;600;700&family=Nunito:wght@800;900&family=Open+Sans:wght@400;600&display=swap">
<style>
  :root{
    --terracotta:#b9705d;
    --navy:#323c4b;
    --mist:#eceef1;
    --white:#ffffff;
    --ink:#2e3845;
    --photo-dark:#26303d;
    --photo-mid:#55606f;
    --photo-warm:#c79a82;
  }
  *{margin:0;padding:0;box-sizing:border-box}
  html,body{width:950px;height:1200px;overflow:hidden;background:var(--white)}
  .flyer{position:relative;width:950px;height:1200px;overflow:hidden;background:var(--white);font-family:"Open Sans",sans-serif;color:var(--ink)}

  .hero-shapes{position:absolute;left:0;top:0}
  .hero-photo{position:absolute;left:395px;top:40px;width:555px;height:505px;border-radius:280px 0 0 0;
    background:radial-gradient(ellipse at 75% 35%,var(--photo-warm) 0%,var(--photo-mid) 45%,var(--photo-dark) 100%)}

  .brand{position:absolute;left:46px;top:52px;display:flex;align-items:center;gap:14px}
  .brand-mark{width:34px;height:34px;border:4px solid var(--terracotta)}
  .brand-name{font-family:"Poppins",sans-serif;font-weight:600;font-size:27px;line-height:1.05;color:var(--terracotta)}

  .headline{position:absolute;left:46px;top:208px;font-family:"Poppins",sans-serif;font-weight:400;font-size:46px;line-height:59px;color:var(--navy);z-index:2}
  .headline span{display:block}
  .headline .strong{font-weight:700}
  .headline .accent{font-weight:700;color:var(--terracotta)}

  .features{position:absolute;top:575px;left:0;width:950px}
  .feature{position:absolute;width:180px;margin-left:-90px;text-align:center}
  .feature-icon{display:block;margin:0 auto}
  .feature-label{display:block;margin-top:14px;font-size:17px;color:var(--ink)}

  .about{position:absolute;left:46px;top:718px;width:420px}
  h2{font-family:"Nunito",sans-serif;font-weight:900;font-size:32px;line-height:1.2}
  h2 .accent{color:var(--terracotta)}
  h2 .dark{color:var(--navy)}
  .about p{font-size:16px;line-height:26.6px;margin-top:2px}
  .about p + p{margin-top:18px}

  .call{position:absolute;left:61px;top:981px;width:232px;text-align:center}
  .call-title{font-family:"Nunito",sans-serif;font-weight:800;font-size:20px;color:var(--navy)}
  .call-pill{margin-top:4px;height:61px;border-radius:31px;border:2px solid var(--navy);padding:3px}
  .call-pill span{display:block;height:100%;border-radius:28px;background:var(--terracotta);color:var(--white);
    font-family:"Nunito",sans-serif;font-weight:900;font-size:24px;line-height:51px}

  .experience{position:absolute;left:493px;top:720px;width:420px}
  .experience ul{list-style:none;margin-top:6px}
  .experience li{position:relative;padding-left:39px;font-size:17px;line-height:31px}
  .experience li::before{content:"";position:absolute;left:13px;top:13px;width:7px;height:7px;border:1.5px solid var(--terracotta);border-radius:50%}

  .services{position:absolute;left:502px;top:853px;width:391px;height:216px;background:var(--terracotta);border-radius:16px 0 6px 0}
  .services-tab{position:absolute;left:-16px;top:17px;width:284px;height:56px;background:var(--navy);border-radius:14px 0 12px 0;
    font-family:"Nunito",sans-serif;font-weight:900;font-size:31px;line-height:56px;color:var(--white);padding-left:42px}
  .services ul{position:absolute;left:26px;top:88px;list-style:none}
  .services li{position:relative;padding-left:18px;font-family:"Nunito",sans-serif;font-weight:800;font-style:italic;font-size:19.5px;line-height:40.5px;color:var(--white);white-space:nowrap}
  .services li::before{content:"";position:absolute;left:0;top:17px;width:6px;height:6px;border-radius:50%;background:var(--white)}

  .contact-band{position:absolute;left:2px;top:1089px;width:415px;height:111px;background:var(--terracotta);border-radius:0 70px 0 0}
  .contact-panel{position:absolute;left:2px;top:1106px;width:440px;height:78px;background:var(--navy);border-radius:0 39px 39px 0}
  .contact-panel ul{list-style:none;padding:8px 0 0 62px}
  .contact-panel li{position:relative;padding-left:20px;font-size:17px;line-height:31px;color:var(--white)}
  .contact-panel li::before{content:"";position:absolute;left:0;top:11px;width:11px;height:11px;border-radius:50%;background:var(--terracotta)}

  .stat{position:absolute;top:1106px;width:140px;margin-left:-70px;height:78px}
  .stat-disc{position:absolute;left:32px;top:0;width:76px;height:76px;border-radius:50%;background:var(--navy)}
  .stat-band{position:absolute;left:0;top:32px;width:140px;height:26px;background:var(--white)}
  .stat-value{position:absolute;left:0;top:9px;width:140px;text-align:center;font-family:"Nunito",sans-serif;font-weight:900;font-size:17px;color:var(--terracotta)}
  .stat-label{position:absolute;left:0;top:29px;width:140px;text-align:center;font-size:18px;color:var(--ink)}
</style>
</head>
<body>
<main class="flyer">

  <svg class="hero-shapes" width="950" height="545" viewBox="0 0 950 545" aria-hidden="true">
    <path d="M0 125 L125 0 H440 V545 H0 Z" fill="var(--mist)"/>
    <path d="M437 0 H950 V545 H560 C470 420 405 200 437 0 Z" fill="var(--navy)"/>
  </svg>
  <div class="hero-photo" role="img" aria-label="Photo of two smiling business professionals reviewing a tablet together"></div>

  <div class="brand">
    <span class="brand-mark"></span>
    <span class="brand-name">Brightfen<br>Ledger Works</span>
  </div>

  <h1 class="headline">
    <span>PROFESSIONAL</span>
    <span class="strong">ESCROW</span>
    <span class="accent">RECONCILIATION</span>
    <span>SERVICES</span>
  </h1>

  <section class="features">
    <div class="feature" style="left:195px">
      <svg class="feature-icon" width="72" height="72" viewBox="0 0 72 72" aria-hidden="true">
        <circle cx="36" cy="36" r="34" fill="none" stroke="var(--terracotta)" stroke-width="3"/>
        <g fill="none" stroke="var(--terracotta)" stroke-width="1.8" stroke-linejoin="round">
          <rect x="21" y="18" width="24" height="32" rx="2"/>
          <path d="M26 28 l5 -4 l5 4 l5 -4"/>
          <path d="M25 40 h12 M25 44 h10"/>
          <circle cx="46" cy="44" r="5"/>
        </g>
      </svg>
      <span class="feature-label">2 Way Reconciliation</span>
    </div>
    <div class="feature" style="left:385px">
      <svg class="feature-icon" width="72" height="72" viewBox="0 0 72 72" aria-hidden="true">
        <circle cx="36" cy="36" r="34" fill="none" stroke="var(--terracotta)" stroke-width="3"/>
        <g fill="none" stroke="var(--terracotta)" stroke-width="1.8" stroke-linejoin="round">
          <rect x="18" y="20" width="32" height="26" rx="2"/>
          <path d="M18 27 h32"/>
          <path d="M27 34 l-3 3 l3 3 M33 34 l3 3 l-3 3"/>
          <circle cx="47" cy="45" r="5"/>
        </g>
      </svg>
      <span class="feature-label">Software System</span>
    </div>
    <div class="feature" style="left:575px">
      <svg class="feature-icon" width="72" height="72" viewBox="0 0 72 72" aria-hidden="true">
        <circle cx="36" cy="36" r="34" fill="none" stroke="var(--terracotta)" stroke-width="3"/>
        <g fill="none" stroke="var(--terracotta)" stroke-width="1.8" stroke-linejoin="round">
          <rect x="27" y="22" width="24" height="13" rx="1.5"/>
          <circle cx="39" cy="28.5" r="3"/>
          <path d="M17 40 h6 c5 0 8 3 12 3 h9 c3 0 4 -3 7 -3"/>
          <path d="M17 47 h8 c6 0 12 2 18 -1"/>
        </g>
      </svg>
      <span class="feature-label">Affordable Price</span>
    </div>
    <div class="feature" style="left:765px">
      <svg class="feature-icon" width="72" height="72" viewBox="0 0 72 72" aria-hidden="true">
        <circle cx="36" cy="36" r="34" fill="none" stroke="var(--terracotta)" stroke-width="3"/>
        <g fill="none" stroke="var(--terracotta)" stroke-width="1.8" stroke-linejoin="round">
          <path d="M24 18 h18 l6 6 v28 h-24 Z"/>
          <path d="M28 28 h3 v3 h-3 Z M28 35 h3 v3 h-3 Z M28 42 h3 v3 h-3 Z"/>
          <path d="M34 29.5 h9 M34 36.5 h9 M34 43.5 h9"/>
        </g>
      </svg>
      <span class="feature-label">Daily Reports</span>
    </div>
  </section>

  <section class="about">
    <h2><span class="accent">About</span> <span class="dark">Us</span></h2>
    <p>For professionals in the title insurance industry, finding a reliable and cost-effective solution to escrow accounting needs can feel overwhelming. Title companies and law firms need an accounting partner they can trust, and that’s where we come in.</p>
    <p>Experienced, convenient and cost-effective, nationwide.</p>
  </section>

  <div class="call">
    <div class="call-title">Call Today</div>
    <div class="call-pill"><span>0909 0011 587</span></div>
  </div>

  <section class="experience">
    <h2><span class="accent">Experiences</span> <span class="dark">Way</span></h2>
    <ul>
      <li>Secure in Escrow Accounting</li>
      <li>Expert Accounting Team</li>
    </ul>
  </section>

  <section class="services">
    <div class="services-tab">Our Services</div>
    <ul>
      <li>Escrow Reconciliation Services</li>
      <li>NTSA Best Practice Certification</li>
      <li>Other Related Services</li>
    </ul>
  </section>

  <div class="contact-band"></div>
  <div class="contact-panel">
    <ul>
      <li>brightfenledgerworks.com</li>
      <li>mail@brightfenledgerworks.com</li>
    </ul>
  </div>

  <div class="stat" style="left:529px">
    <div class="stat-disc"></div><div class="stat-band"></div>
    <div class="stat-value">100%</div><div class="stat-label">Compliance</div>
  </div>
  <div class="stat" style="left:700px">
    <div class="stat-disc"></div><div class="stat-band"></div>
    <div class="stat-value">100%</div><div class="stat-label">Convenience</div>
  </div>
  <div class="stat" style="left:865px">
    <div class="stat-disc"></div><div class="stat-band"></div>
    <div class="stat-value">100%</div><div class="stat-label">Credibility</div>
  </div>

</main>
</body>
</html>
```